Professional violinist needs business cards

I am trying to attract the following jobs:
-private violin lessons (primarily classical)
-performance gigs (weddings, birthday parties, funerals, etc.)
-collaborations with other artists (studio recordings, performances)

I want to communicate that I have a very high standard of excellence for my work, but I also love people and celebrations.
Values/style words I like are:
love, joy, peace, fun, beauty, authenticity, excellence, warmth, refined/sleek, free spirited. If that's too confusing, just ignore :)

I will attach my favorite business card template that I could find on Canva. The lines are supposed to be like a music staff, which I think is really cool, but I also don't want it to look too busy. I like the simple black and white--I think it looks sharp--but I also am open to other ideas. I also have seen business cards with pictures included that looked great, so I attached an image that could be used as well.

I am also attaching a file that I made of my initials that could be used as a logo, but I'm not sure if it should be included.

Information on the card:
-My name (18 letters total)
-"violinist"
-phone number, email, website

Thank you!

```html
<!DOCTYPE html>
<html lang="en">
<head>
<meta charset="utf-8">
<title>Elena Marlowe – Violinist Business Cards</title>
<link href="https://fonts.googleapis.com/css2?family=Raleway:wght@500;600&family=Open+Sans:wght@400&display=swap" rel="stylesheet">
<style>
  :root {
    --bg: #2b2b2b;
    --card-black: #000000;
    --panel-grey: #1e1e1e;
    --gold: #d19a35;
    --white: #ffffff;
    --photo-top: #3a2a22;
    --photo-bottom: #141414;
  }
  * { box-sizing: border-box; margin: 0; padding: 0; }
  html, body {
    width: 1200px; height: 900px; overflow: hidden;
    background: var(--bg);
  }
  .canvas {
    position: relative; width: 1200px; height: 900px;
  }
  .card {
    position: absolute; left: 280px; width: 640px; height: 366px;
    background: var(--card-black); overflow: hidden;
    box-shadow: 0 10px 30px rgba(0,0,0,.55);
  }
  .card--front { top: 54px; }
  .card--back { top: 480px; }

  /* Front */
  .staff { position: absolute; inset: 0; width: 100%; height: 100%; }
  .staff line { stroke: var(--gold); stroke-width: 3; }
  .brand {
    position: absolute; left: 30px; top: 138px;
    display: flex; align-items: center; gap: 16px;
    background: var(--card-black); padding: 10px 18px 10px 12px;
  }
  .brand__dot {
    width: 34px; height: 34px; border-radius: 50%;
    background: var(--gold);
  }
  .brand__name {
    font-family: "Raleway", sans-serif; font-weight: 600;
    font-size: 52px; color: var(--gold); letter-spacing: 1px;
  }
  .front__web {
    position: absolute; right: 26px; bottom: 44px;
    background: var(--card-black); padding: 0 6px;
    font-family: "Open Sans", sans-serif; font-size: 13px;
    color: var(--white); letter-spacing: 1px;
  }

  /* Back */
  .back__panel {
    position: absolute; top: 0; right: 0; width: 255px; height: 100%;
    background: var(--panel-grey);
  }
  .back__photo {
    position: absolute; top: 20px; right: 30px; width: 200px; height: 346px;
    background: linear-gradient(180deg, var(--photo-top) 0%, #2a1e1a 45%, var(--photo-bottom) 100%);
    border-radius: 90px 90px 0 0;
  }
  .identity {
    position: absolute; right: 262px; top: 178px; text-align: right;
  }
  .identity__name {
    font-family: "Raleway", sans-serif; font-weight: 500;
    font-size: 27px; color: var(--gold); letter-spacing: .5px;
  }
  .identity__role {
    font-family: "Raleway", sans-serif; font-weight: 500;
    font-size: 14px; color: var(--white); margin-top: -2px;
  }
  .contact {
    position: absolute; left: 40px; bottom: 30px; list-style: none;
    font-family: "Open Sans", sans-serif; font-size: 15px; color: var(--white);
  }
  .contact__item {
    display: flex; align-items: center; gap: 16px; height: 24px;
  }
  .contact__icon { width: 16px; height: 16px; fill: var(--gold); }
</style>
</head>
<body>
<main class="canvas">

  <section class="card card--front" aria-label="Card front">
    <svg class="staff" viewBox="0 0 640 366" preserveAspectRatio="none" aria-hidden="true">
      <line x1="0" y1="40" x2="640" y2="40"/>
      <line x1="0" y1="92" x2="640" y2="92"/>
      <line x1="0" y1="144" x2="640" y2="144"/>
      <line x1="0" y1="196" x2="640" y2="196"/>
      <line x1="0" y1="248" x2="640" y2="248"/>
      <line x1="0" y1="300" x2="640" y2="300"/>
    </svg>
    <div class="brand">
      <span class="brand__dot"></span>
      <span class="brand__name">Elena Marlowe</span>
    </div>
    <p class="front__web">www.marloweviolin.com</p>
  </section>

  <section class="card card--back" aria-label="Card back">
    <div class="back__panel"></div>
    <div class="back__photo" role="img" aria-label="Portrait photo of the violinist in a black dress holding her violin and bow"></div>
    <div class="identity">
      <h1 class="identity__name">Elena Marlowe</h1>
      <p class="identity__role">Violinist</p>
    </div>
    <ul class="contact">
      <li class="contact__item">
        <svg class="contact__icon" viewBox="0 0 16 16" aria-hidden="true"><path d="M1 5c0-2 3-3 7-3s7 1 7 3v1h-4V5H5v1H1z"/><path d="M4 7h8l2 7H2z"/></svg>
        012 555 0148
      </li>
      <li class="contact__item">
        <svg class="contact__icon" viewBox="0 0 16 16" aria-hidden="true"><path d="M1 3h14v10H1z M2.5 4.5 8 9l5.5-4.5" stroke="#000" stroke-width="1.2"/></svg>
        hello@marloweviolin.com
      </li>
      <li class="contact__item">
        <svg class="contact__icon" viewBox="0 0 16 16" aria-hidden="true"><circle cx="8" cy="8" r="7"/><path d="M1 8h14M8 1c3 3 3 11 0 14M8 1c-3 3-3 11 0 14" stroke="#000" stroke-width="1" fill="none"/></svg>
        www.marloweviolin.com
      </li>
    </ul>
  </section>

</main>
</body>
</html>
```